Manufacturing company needs new business card.

I need a unique Business Card that will truly stand out. Nothing too busy. Simple is good, right? Not looking for a standard design either. No cookie cutter layout. I am just looking for something interesting and a bit different. Does't have to completely off the wall crazy, just not your run of the mill business card. Clean and modern with a touch of industrial.

Target Market(s)

Air conditioning industry, Architects, builders.

Industry/Entity Type

Business

Contact Information for Business Card

Details to be included on card are:

Peter Vance
Managing Director

T: 1300 847 519
M: 0428 593 174
W: www.brenvaleworks.com.au
E: peter.vance@brenvaleworks.com.au
A: 58 Harwick Lane, Sydney NSW 2000

Font styles to use
Sans Serif

Colors
0355a3
848484
fbfbfb

Requirements
Must have
• Card design must be landscape.

```html
<!DOCTYPE html>
<html lang="en">
<head>
<meta charset="utf-8">
<title>Brenvale Works Australia – Business Card</title>
<link href="https://fonts.googleapis.com/css2?family=Open+Sans:wght@400;600;700&display=swap" rel="stylesheet">
<style>
  :root {
    --brand-blue: #0355a3;
    --band-blue: #1f4fa6;
    --steel-grey: #848484;
    --paper: #fbfbfb;
    --ink-grey: #6e6e6e;
    --backdrop: #2a2a2c;
    --icon-grey: #8a8a8a;
  }
  * { margin: 0; padding: 0; box-sizing: border-box; }
  html, body {
    width: 1200px; height: 900px; overflow: hidden;
    background: var(--backdrop);
    font-family: "Open Sans", Arial, sans-serif;
  }
  .stage { position: relative; width: 1200px; height: 900px; }

  .card {
    position: absolute; width: 540px; height: 320px;
    border-radius: 18px; overflow: hidden;
  }

  /* Back of card */
  .card-back { left: 70px; top: 110px; background: var(--steel-grey); color: #fff; }
  .card-back .wordmark {
    position: absolute; left: 120px; top: 112px;
    display: flex; align-items: center; gap: 14px;
  }
  .card-back .mark-square { width: 34px; height: 34px; background: #fff; }
  .card-back .brand-name { font-size: 34px; font-weight: 600; letter-spacing: .3px; }
  .card-back .brand-rule {
    position: absolute; left: 168px; top: 168px; width: 120px; height: 2px; background: #fff;
  }
  .card-back .brand-region {
    position: absolute; left: 300px; top: 158px;
    font-size: 15px; letter-spacing: 7px;
  }
  .card-back .web-line {
    position: absolute; left: 250px; right: 0; top: 252px;
    display: flex; align-items: center; gap: 10px;
  }
  .card-back .web-line .web-address { font-size: 14px; }
  .card-back .web-line .rule { flex: 1; height: 2px; background: #fff; }
  .card-back .base-rule {
    position: absolute; left: 0; right: 0; top: 278px; height: 2px; background: #fff;
  }

  /* Front of card */
  .card-front { left: 590px; top: 470px; background: var(--paper); }
  .card-front .band { position: absolute; inset: 0; }
  .card-front .wordmark {
    position: absolute; left: 30px; top: 132px;
    display: flex; align-items: center; gap: 10px;
  }
  .card-front .mark-square { width: 26px; height: 26px; background: var(--brand-blue); }
  .card-front .brand-name { font-size: 24px; font-weight: 600; color: var(--brand-blue); white-space: nowrap; }
  .card-front .brand-rule {
    position: absolute; left: 66px; top: 172px; width: 76px; height: 2px; background: var(--ink-grey);
  }
  .card-front .brand-region {
    position: absolute; left: 150px; top: 164px;
    font-size: 11px; letter-spacing: 5px; color: var(--ink-grey);
  }
  .contact-block {
    position: absolute; right: 22px; top: 60px; text-align: right; color: #fff;
  }
  .contact-block .person-name {
    font-size: 19px; font-weight: 700; color: var(--brand-blue); line-height: 26px;
  }
  .contact-block .person-title { font-size: 13px; margin-top: 8px; margin-right: 22px; }
  .contact-list { list-style: none; margin-top: 12px; }
  .contact-list li {
    display: flex; justify-content: flex-end; align-items: center; gap: 6px;
    font-size: 12.5px; line-height: 20px; white-space: nowrap;
  }
  .contact-list li .icon {
    width: 16px; height: 16px; border-radius: 50%;
    background: var(--icon-grey); display: inline-flex; align-items: center; justify-content: center;
  }
</style>
</head>
<body>
<main class="stage">

  <section class="card card-back" aria-label="Business card back">
    <div class="wordmark">
      <span class="mark-square"></span>
      <span class="brand-name">Brenvale Works</span>
    </div>
    <div class="brand-rule"></div>
    <div class="brand-region">AUSTRALIA</div>
    <div class="web-line">
      <span class="rule"></span>
      <span class="web-address">www.brenvaleworks.com.au</span>
      <span class="rule"></span>
    </div>
    <div class="base-rule"></div>
  </section>

  <section class="card card-front" aria-label="Business card front">
    <svg class="band" width="540" height="320" viewBox="0 0 540 320" aria-hidden="true">
      <polygon points="268,90 540,90 540,320 0,320 0,232 268,232" fill="var(--band-blue)"/>
    </svg>
    <div class="wordmark">
      <span class="mark-square"></span>
      <span class="brand-name">Brenvale Works</span>
    </div>
    <div class="brand-rule"></div>
    <div class="brand-region">AUSTRALIA</div>

    <div class="contact-block">
      <div class="person-name">Peter Vance</div>
      <div class="person-title">Managing Director</div>
      <ul class="contact-list">
        <li>1300 847 519
          <span class="icon"><svg width="10" height="10" viewBox="0 0 10 10"><path d="M2 1l2 2-1 1.2c.6 1.2 1.6 2.2 2.8 2.8L7 6l2 2-1.2 1.2C4.5 9 1 5.5.8 2.2z" fill="#fff"/></svg></span>
        </li>
        <li>0428 593 174
          <span class="icon"><svg width="10" height="10" viewBox="0 0 10 10"><rect x="2.5" y="0.5" width="5" height="9" rx="1" fill="#fff"/><rect x="3.5" y="1.8" width="3" height="5" fill="#8a8a8a"/></svg></span>
        </li>
        <li>peter.vance@brenvaleworks.com.au
          <span class="icon"><svg width="10" height="10" viewBox="0 0 10 10"><rect x="1" y="2.5" width="8" height="5.5" fill="#fff"/><path d="M1 2.5l4 3 4-3" stroke="#8a8a8a" stroke-width=".8" fill="none"/></svg></span>
        </li>
        <li>58 Harwick Lane, Sydney NSW 2000
          <span class="icon"><svg width="10" height="10" viewBox="0 0 10 10"><path d="M5 .8a3 3 0 0 1 3 3c0 2.2-3 5.4-3 5.4S2 6 2 3.8a3 3 0 0 1 3-3z" fill="#fff"/><circle cx="5" cy="3.8" r="1.1" fill="#8a8a8a"/></svg></span>
        </li>
      </ul>
    </div>
  </section>

</main>
</body>
</html>
```